Contemporary update for a market leader in foodservice distribution

KORLO is a market leader in foodservice distribution nationwide.
We have recently adopted a new look and feel for our flagship foodservice rewards programme, and we're looking to have our business cards reflect our new aesthetic. Below is a link to our new rewards website to give you a general idea on the look we're after. https://korlotierclub.com.au/

Industry/Entity Type

Distribution

Contact Information for Business Card

Must have space for contact name, position, company name and ABN, address, phone number and direct number, fax, email, and web address.

Font styles to use
Serif
Sans Serif

Requirements
Must have
• We'd like a landscape design, with our 'Bright Ember Tier' logo incorporated on either the front or the back of the card. The overall design should be contemporary and professional.
Nice to have
• I have included both the full colour and white version of our company logo - our preference is to have the company logo one solid colour (white, or a shade of grey) although we're also open to designs including the full colour logo. If you are able to incorporate a small Chatterleaf and Workmesh logo, please do so.
Should not have
• Should not have an over-complicated design. No images of globes, or food.

```html
<!DOCTYPE html>
<html lang="en">
<head>
<meta charset="utf-8">
<title>KORLO Business Card</title>
<link rel="stylesheet" href="https://fonts.googleapis.com/css2?family=Arimo:wght@400;700&family=Cinzel:wght@400&family=Open+Sans:wght@700&display=swap">
<style>
  :root {
    --page: #e9e9e7;
    --green: #17a852;
    --green-deep: #0b8a55;
    --grey-stripe: #a3a3a3;
    --white: #ffffff;
    --ink: #1b1b1b;
    --black: #000000;
    --yellow: #fbe710;
  }
  html, body {
    margin: 0;
    padding: 0;
    width: 1200px;
    height: 933px;
    overflow: hidden;
    background: var(--page);
  }
  .canvas {
    position: relative;
    width: 1200px;
    height: 933px;
  }
  .card {
    position: absolute;
    left: 274px;
    width: 652px;
    height: 374px;
    overflow: hidden;
    box-shadow: 0 4px 14px rgba(0,0,0,0.25);
  }
  .card--front { top: 64px; background: var(--white); }
  .card--back { top: 494px; background: var(--black); }

  .front-shape { position: absolute; inset: 0; }

  .tier-mark {
    position: absolute;
    left: 34px;
    top: 150px;
    display: flex;
    align-items: center;
    gap: 10px;
  }
  .tier-mark__dot {
    width: 40px;
    height: 40px;
    border-radius: 50%;
    background: var(--green);
    flex: none;
  }
  .tier-mark__name {
    font-family: "Arimo", sans-serif;
    font-weight: 700;
    font-size: 23px;
    color: var(--ink);
    line-height: 1.1;
    width: 150px;
  }

  .contact {
    position: absolute;
    left: 387px;
    top: 62px;
    color: var(--white);
    font-family: "Arimo", sans-serif;
  }
  .contact__name { font-size: 29px; font-weight: 700; margin: 0; line-height: 1; }
  .contact__role { font-size: 17px; margin: 6px 0 0; }
  .contact__address { font-size: 17px; margin: 34px 0 0; line-height: 20px; }
  .contact__list { list-style: none; padding: 0; margin: 30px 0 0; font-size: 17px; line-height: 21px; }
  .contact__list li { display: flex; align-items: center; gap: 10px; }
  .contact__icon { width: 12px; height: 12px; flex: none; }

  .brand {
    position: absolute;
    left: 98px;
    top: 104px;
    display: flex;
    align-items: center;
    gap: 26px;
  }
  .brand__dot {
    width: 86px;
    height: 86px;
    border-radius: 50%;
    background: var(--green-deep);
    flex: none;
  }
  .brand__name {
    font-family: "Cinzel", serif;
    font-size: 72px;
    color: var(--white);
    letter-spacing: 2px;
    line-height: 1;
  }
  .tagline {
    position: absolute;
    left: 226px;
    top: 198px;
    font-family: "Open Sans", sans-serif;
    font-weight: 700;
    font-size: 13.5px;
    letter-spacing: 0.8px;
    color: var(--white);
  }
  .abn {
    position: absolute;
    left: 246px;
    top: 238px;
    font-family: "Arimo", sans-serif;
    font-size: 17px;
    color: var(--white);
  }
  .stripe { position: absolute; left: 0; top: 308px; width: 652px; height: 13px; }
</style>
</head>
<body>
<main class="canvas">
  <section class="card card--front">
    <svg class="front-shape" width="652" height="374" viewBox="0 0 652 374" aria-hidden="true">
      <path d="M352 0 C 370 140 300 270 170 374 L 186 374 C 312 270 382 140 364 0 Z" fill="var(--grey-stripe)"/>
      <path d="M372 0 C 390 140 320 270 210 374 L 652 374 L 652 0 Z" fill="var(--green)"/>
    </svg>

    <div class="tier-mark">
      <span class="tier-mark__dot"></span>
      <span class="tier-mark__name">Bright Ember Tier</span>
    </div>

    <div class="contact">
      <p class="contact__name">Marcus Pellow</p>
      <p class="contact__role">Managing Director</p>
      <p class="contact__address">Tarrow Lane, Bristol<br>United Kingdom</p>
      <ul class="contact__list">
        <li><svg class="contact__icon" viewBox="0 0 12 12"><rect width="12" height="12" fill="#fff"/><path d="M3 4h6v1.5H3zM4 6.5h4v3H4z" fill="var(--green)"/></svg>555-210-4417</li>
        <li><svg class="contact__icon" viewBox="0 0 12 12"><rect width="12" height="12" fill="#fff"/><rect x="4" y="2" width="4" height="8" fill="var(--green)"/></svg>555-210-4480</li>
        <li><svg class="contact__icon" viewBox="0 0 12 12"><rect width="12" height="12" fill="#fff"/><rect x="3" y="3" width="6" height="2" fill="var(--green)"/><rect x="3" y="7" width="6" height="2" fill="var(--green)"/></svg>555-210-4499</li>
        <li><svg class="contact__icon" viewBox="0 0 12 12"><rect width="12" height="12" fill="#fff"/><path d="M2 3h8v6H2z" fill="none" stroke="var(--green)"/><path d="M2 3l4 3 4-3" fill="none" stroke="var(--green)"/></svg>hello@korlotrade.com</li>
        <li><svg class="contact__icon" viewBox="0 0 12 12"><rect width="12" height="12" fill="#fff"/><circle cx="6" cy="6" r="3.5" fill="none" stroke="var(--green)"/></svg>www.korlotrade.com</li>
      </ul>
    </div>
  </section>

  <section class="card card--back">
    <div class="brand">
      <span class="brand__dot"></span>
      <span class="brand__name">KORLO</span>
    </div>
    <p class="tagline">AUSTRALIAN FOODSERVICE DISTRIBUTION</p>
    <p class="abn">ABN: 41 208 663 590</p>
    <svg class="stripe" viewBox="0 0 652 13" aria-hidden="true">
      <path d="M0 0 H305 L309 13 H0 Z" fill="var(--yellow)"/>
      <path d="M310 0 H652 V13 H315 Z" fill="var(--green-deep)"/>
    </svg>
  </section>
</main>
</body>
</html>
```